Fenwick Creek Rodeo Sponsor Brochure/letter

We are wanting a professional looking brochure/letter that can be given to potential sponsors. This can be multiple pages the last page needs to be the Invoice (attached example) the prices on the example can be used.. this is a first nation rodeo and we are looking for sponsorship I can provide more photos if needed

Target Market(s)

This will be local corporate business's so this needs to be very professional looking

Industry/Entity Type

This is an event but we are looking for cooperate sponsorship

Font styles to use
Serif

Colors
0054AA
0677BA
7BADD7
CADEEF
E8F1F8
FFC000
F8CF3A
FAE287
FDF2CF
FEFAEE
F0912C
F2A743
F7CA91
FBE8D2
FDF5EE
EB3D1F
EC4F4E
F09395
F8D3D4
FCEDEE

Requirements
Must have
• The basic information, must have some quotes and photos can be multiple pages
Nice to have
• I would like to see that it is interactive, but gets to the point
Should not have
• no cartoon or must not look cheap

```html
<!DOCTYPE html>
<html lang="en">
<head>
<meta charset="utf-8">
<title>Fenwick Creek Rodeo – Sponsorship Proposal</title>
<link href="https://fonts.googleapis.com/css2?family=Montserrat:wght@400;500;600;700;800&display=swap" rel="stylesheet">
<style>
:root{
  --blue:#1f4e7d;
  --blue-dark:#1a426b;
  --green:#84a92a;
  --page:#f4f4f4;
  --card:#dcdcdc;
  --ink:#2a2a2a;
  --rule:#9a9a9a;
}
*{box-sizing:border-box;margin:0;padding:0}
html,body{width:940px;height:1200px;overflow:hidden;background:#fff}
body{position:relative;font-family:"Montserrat",Arial,sans-serif;color:var(--ink)}
.page{position:absolute;width:384px;height:496px;background:var(--page);box-shadow:0 2px 10px rgba(0,0,0,.12);overflow:hidden}
.abs{position:absolute}
.p1{left:69px;top:82px}
.p2{left:488px;top:82px}
.p3{left:66px;top:630px}
.p4{left:488px;top:630px}

/* brand name stand-in */
.brand{display:flex;align-items:center;gap:6px;color:var(--blue);font-weight:600;line-height:1.05}
.brand .dot{width:22px;height:22px;border-radius:50%;background:var(--green);flex:none}
.brand .name{font-size:15px}
.brand .sub{font-size:7px;font-weight:600;letter-spacing:.2px}
.brand-sm .dot{width:9px;height:9px}
.brand-sm .name{font-size:6px}
.brand-sm .sub{font-size:3px}

/* page 1 */
.cover-band{left:19px;top:109px;width:74px;height:254px;background:var(--green);overflow:hidden}
.cover-title{position:absolute;left:9px;top:0;height:254px;padding-top:12px;
  writing-mode:vertical-rl;transform:rotate(180deg);color:#fff;font-weight:800;text-transform:uppercase;white-space:nowrap}
.cover-title .line-small{display:block;font-size:16.5px;line-height:18px}
.cover-title .line-big{display:block;font-size:39px;line-height:38px}
.photo{background:linear-gradient(160deg,#35507a,#1c2f4a)}
.photo.tan{background:linear-gradient(160deg,#8d7a5c,#c9a57a 60%,#6d5a42)}
.photo.sky{background:linear-gradient(160deg,#5f7ea6,#c9b08d 70%,#8f7a5f)}
.photo.night{background:linear-gradient(160deg,#2a4660,#17293a)}
.intro{left:46px;top:390px;width:292px;font-size:5.8px;line-height:1.35;text-align:center}
.site{font-weight:600;color:var(--blue);letter-spacing:.3px;text-align:center}
.site b{color:var(--green);font-weight:600}
.p1 .site{left:0;width:384px;top:450px;font-size:21px}

/* page 2 */
.hero{left:19px;top:17px;width:346px;height:118px;background:linear-gradient(170deg,#4f6b45 0%,#8b7a62 40%,#5a4334 70%,#6a7f4a 100%)}
.quote{left:19px;top:135px;width:346px;height:42px;background:var(--green);color:#fff;padding:6px 10px}
.quote .q{font-size:9.4px;font-weight:500}
.quote .q::before{content:"\201C";font-size:14px;font-weight:800;margin-right:5px;vertical-align:-3px}
.quote .q::after{content:"\201D";font-size:14px;font-weight:800;margin-left:6px;vertical-align:-6px}
.quote .by{text-align:right;font-size:10px;font-weight:800;margin-top:4px;letter-spacing:.3px}
.story{left:19px;top:178px;width:346px;height:132px;background:var(--blue);color:#fff;padding:9px 10px;font-size:5.1px;line-height:1.2}
.story p+p{margin-top:5px}
.h-green{color:var(--green);font-weight:800;font-size:10px}
.small-blue{color:var(--blue);font-size:5.8px}
.small{font-size:5.8px}
.contact{display:flex;gap:14px;font-size:6px;font-weight:600;align-items:center;margin-top:6px}
.contact span{display:flex;align-items:center;gap:4px}
.dates{left:230px;top:342px;width:128px;height:24px;border-radius:5px;background:var(--blue);color:#fff;font-weight:800;font-size:10.5px;display:flex;align-items:center;justify-content:center}
.events{left:19px;top:394px;width:180px;font-size:5.4px;line-height:1.25;list-style:none}
.events li{position:relative;padding-left:7px;margin-bottom:3px}
.events li::before{content:"";position:absolute;left:0;top:1.5px;width:3px;height:3px;border-radius:50%;background:var(--blue)}
.blurb{left:205px;top:394px;width:160px;font-size:5.4px;line-height:1.22}
.dance{left:205px;top:440px;color:var(--blue);font-weight:800;font-size:7.4px;line-height:1.2}
.foot-blue{left:0;width:262px;height:6px;background:var(--blue)}
.foot-green{left:329px;width:55px;height:6px;background:var(--green)}

/* page 3 */
.card{background:var(--card);border-radius:6px;padding:7px 5px}
.tag{height:14px;border-radius:2px;font-size:6.2px;font-weight:700;display:flex;align-items:center;justify-content:center;color:#222;margin:0 2px 8px}
.tag.bronze{background:linear-gradient(90deg,#b94f22,#e08a4a)}
.tag.silver{background:linear-gradient(90deg,#8c8c8c,#d8d8d8)}
.tag.gold{background:linear-gradient(90deg,#b8912e,#efd57a)}
.tag.plat{background:linear-gradient(90deg,#b5b5b5,#e9e9e9)}
.tag.blue{background:var(--blue);color:#fff;height:17px;font-size:6.6px;margin:4px 12px 10px}
.tag.green{background:var(--green);color:#fff;height:17px;font-size:6.2px;line-height:1.05;text-align:center;margin:4px 12px 10px}
.tag.wide{margin:4px 6px 10px;height:15px}
.list{list-style:none;font-size:4.3px;line-height:1.2}
.list li{position:relative;padding-left:6px;margin-bottom:4.5px}
.list li::before{content:"";position:absolute;left:0;top:1px;width:2.6px;height:2.6px;border-radius:50%;background:var(--blue)}
.list li.nb::before{display:none}

/* page 4 */
.inv-head{left:19px;top:17px;width:345px;height:110px;background:#e0e0e0}
.inv-badge{left:19px;top:17px;width:90px;height:110px;background:var(--blue);color:#fff;padding:14px 10px}
.inv-badge .brand{color:#fff}
.inv-badge h2{font-size:8.6px;font-weight:800;line-height:1.2;margin-top:22px}
.fields{left:118px;top:23px;width:230px}
.field{font-size:7px;font-weight:700;height:21px;border-bottom:1px solid #333;padding-top:5px}
.tbl{left:19px;width:345px;background:#e3dcdc}
.tbl .hd{height:14px;background:var(--green);color:#fff;font-size:6.8px;font-weight:800;position:relative}
.tbl .hd span{position:absolute;top:3px}
.tbl .row{height:16px;border-bottom:1px dashed #a7a0a0;position:relative;font-size:5.6px;font-weight:700;margin:0 5px}
.tbl .row span{position:absolute;top:5px}
.tbl .vl{position:absolute;border-left:1px dashed #a7a0a0;top:14px;bottom:6px}
.pay{left:19px;top:386px;width:345px;height:40px;background:var(--blue);color:#fff;font-size:5.6px;font-weight:700}
.p4 .site{left:0;width:384px;top:454px;font-size:21px}
</style>
</head>
<body>

<!-- Page 1: cover -->
<section class="page p1">
  <div class="abs brand" style="left:128px;top:34px">
    <div class="dot"></div>
    <div><div class="name">FENWICK CREEK</div><div class="sub">FIRST NATION · NEHWA KAA DENE</div></div>
  </div>
  <div class="abs cover-band">
    <h1 class="cover-title"><span class="line-small">Rodeo Sponsorship</span><span class="line-big">Proposal</span></h1>
  </div>
  <div class="abs photo" style="left:98px;top:109px;width:130px;height:120px" role="img" aria-label="Rider on horseback seen from behind the grandstand"></div>
  <div class="abs photo sky" style="left:233px;top:109px;width:130px;height:120px" role="img" aria-label="Cowgirl riding a palomino horse past the stands"></div>
  <div class="abs photo tan" style="left:98px;top:232px;width:130px;height:131px" role="img" aria-label="Close view of a galloping palomino in the arena dust"></div>
  <div class="abs photo night" style="left:233px;top:232px;width:130px;height:131px" role="img" aria-label="Dark horse running in evening light"></div>
  <p class="abs intro">Fenwick Creek First Nation (FCFN) is Nehwa Kaa Dene, a proud Tsenah people indigenous to the upper Peace River region of BC and Alberta. Our traditional base extends in all directions from Kah Tah Ni, now called the city of Fort Alder. Today, our members participate in the modern economy while practising our unique language, culture and traditions.</p>
  <div class="abs site">www.<b>fenwickcreekfn</b>.com</div>
</section>

<!-- Page 2: about the rodeo -->
<section class="page p2">
  <div class="abs hero" role="img" aria-label="Bronc rider on a bucking paint horse in the rodeo arena"></div>
  <div class="abs quote">
    <div class="q">Courage is being scared to death and saddling up anyway!</div>
    <div class="by">– WALT HARLAN</div>
  </div>
  <div class="abs story">
    <p>2 One day Rodeos with amazing prizes and buckles each day with the average winning a FCFN Drum! The Fenwick Creek Rodeo is an attraction to many local cowboys and cowgirls from local communities, Fort Alder and across BC, AB and surrounding areas. We offer youth to adult events that are all crowd pleasers.</p>
    <p>Since the beginning this has been an annual event up until Covid-19 when we have had to take a break but we are so excited to build it bigger and better then before!</p>
    <p>We have some big plans for the future of the Fenwick Creek Rodeo including an expansion of the Rodeo grounds, new event buildings, new office/announcer booths as well as the purchase of new grandstands. This will be a big endeavor that we think will benefit both our community as well as the local community.</p>
    <p>Our rodeo would not have flourished without the support and generosity we have received from your sponsorship over the years. Once again, we are hoping your company will give generously to our yearly event and help continue to make our rodeo a success. All support goes towards any supplies not covered by donation, the purchase of materials to upgrade the rodeo grounds, rodeo stock and event payout. We hope to attract even more rodeo events, larger entertainers, and more fans through the gates. Your sponsorship will be highly regarded for what we hope will be generations to come.</p>
  </div>
  <div class="abs" style="left:19px;top:320px;width:210px">
    <div class="h-green">FENWICK CREEK RODEO!</div>
    <div class="small-blue" style="margin-top:3px">Your sponsorship is greatly appreciated.</div>
    <div class="small" style="margin-top:2px">For further information please call or email Dana Whitford</div>
    <div class="contact">
      <span><svg width="7" height="7" viewBox="0 0 24 24"><path fill="#1f4e7d" d="M6.6 10.8a15 15 0 0 0 6.6 6.6l2.2-2.2a1 1 0 0 1 1-.25 11.4 11.4 0 0 0 3.6.57 1 1 0 0 1 1 1V20a1 1 0 0 1-1 1A17 17 0 0 1 3 4a1 1 0 0 1 1-1h3.5a1 1 0 0 1 1 1c0 1.25.2 2.45.57 3.57a1 1 0 0 1-.25 1z"/></svg>250.555.0182</span>
      <span><svg width="8" height="6" viewBox="0 0 24 18"><rect width="24" height="18" rx="2" fill="#1f4e7d"/><path d="M1 2l11 8 11-8" stroke="#fff" stroke-width="2" fill="none"/></svg>mlarose@fenwickcreekfn.com</span>
    </div>
  </div>
  <div class="abs h-green" style="left:231px;top:320px">RODEO DATES:</div>
  <div class="abs dates">JULY 28, 29, 30 2023</div>
  <div class="abs h-green" style="left:19px;top:378px">EVENTS</div>
  <ul class="abs events">
    <li>July 28 Gymkhana and family Dance</li>
    <li>July 29 Junior Rodeo at 11 am, Main Rodeo starts at 2pm with Steak Dinner and Rodeo dance to follow Band is The Cedar Lines</li>
    <li>July 30 Junior Rodeo at 11 am, Main Rodeo starts at 2pm</li>
    <li>Free Pancake Breakfast both Saturday and Sunday Morning</li>
    <li>Cultural Events happening throughout the day</li>
  </ul>
  <p class="abs blurb">Saddle up for the Fenwick Creek Rodeo held at the Fenwick Creek First Nation Rodeo grounds! This is now a 3 day family fun event with the addition of a Friday afternoon Gymkhana! Fenwick Creek Rodeo has been running for over 30 years and we are exciting to bring the excitement back.</p>
  <div class="abs dance">DANCE – JULY 29 THE CEDAR LINES<br>PICTURE PROVIDED</div>
  <div class="abs foot-blue" style="top:480px"></div>
  <div class="abs foot-green" style="top:480px"></div>
  <div class="abs brand brand-sm" style="left:272px;top:467px">
    <div class="dot"></div><div><div class="name">FENWICK</div><div class="sub">FIRST NATION</div></div>
  </div>
</section>

<!-- Page 3: packages -->
<section class="page p3">
  <div class="abs card" style="left:20px;top:16px;width:84px;height:154px">
    <div class="tag bronze">Bronze Package</div>
    <ul class="list"><li>Social media Ads and mentions</li><li>Company logo on Big screen</li><li>Company logo on Web</li><li>4 admission tickets to Sunday Rodeo</li></ul>
  </div>
  <div class="abs card" style="left:107px;top:16px;width:84px;height:154px">
    <div class="tag silver">Silver Package</div>
    <ul class="list"><li>Social media Ads and mentions</li><li>Company logo on Big screen</li><li>Company logo on Web</li><li>Banner (sponsor provided) in arena</li><li>4 weekend passes</li></ul>
  </div>
  <div class="abs card" style="left:194px;top:16px;width:84px;height:154px">
    <div class="tag gold">Gold Package</div>
    <ul class="list"><li>Social media Ads and mentions</li><li>Company logo on Big screen</li><li>Company logo on Web</li><li>Banner (sponsor provided) in arena</li><li>6 weekend passes</li><li>6 Dance tickets (must be age of majority) including steak dinner</li></ul>
  </div>
  <div class="abs card" style="left:281px;top:16px;width:84px;height:154px">
    <div class="tag plat">Platinum Package</div>
    <ul class="list"><li>Pre event Radio advertising</li><li>Company logo on posters</li><li>Social media Ads and mentions</li><li>Company logo on Big screen</li><li>Company logo on Web</li><li>Commercial on the big screen</li><li>2 large Banners (sponsor provided) in arena</li><li>8 weekend passes</li><li>8 Dance tickets (must be age of majority) including steak dinner</li></ul>
  </div>

  <div class="abs card" style="left:20px;top:198px;width:113px;height:84px">
    <div class="tag blue">Starter package</div>
    <ul class="list"><li>Company logo on the big screen</li><li>Company logo on Web and program</li><li class="nb">2 admission tickets to Sunday rodeo</li></ul>
  </div>
  <div class="abs card" style="left:136px;top:198px;width:113px;height:84px">
    <div class="tag green">Pancake Breakfast<br>Package (2 mornings)</div>
    <ul class="list"><li>Social media Ads and mentions</li><li>Company logo on Big screen</li><li>Company logo on Web</li><li class="nb">4 weekend passes</li></ul>
  </div>
  <div class="abs card" style="left:252px;top:198px;width:113px;height:84px">
    <div class="tag blue">Kids Fun Package</div>
    <ul class="list"><li>Company logo on the big screen</li><li>Company logo on Web and program</li><li>Social Media Ads and Mentions</li><li class="nb">2 weekend passes</li></ul>
  </div>

  <div class="abs card" style="left:20px;top:302px;width:170px;height:140px">
    <div class="tag green wide">Saloon Package</div>
    <ul class="list"><li>Pre event Radio advertising</li><li>Company logo on posters</li><li>Social media Ads and mentions</li><li>Company logo on Big screen</li><li>Company logo on Web</li><li>Commercial on the big screen</li><li class="nb">2 large Banners (sponsor provided) in arena</li><li class="nb">6 weekend passes</li><li class="nb">6 Dance tickets (must be age of majority) including steak dinner</li></ul>
  </div>
  <div class="abs card" style="left:194px;top:302px;width:171px;height:140px">
    <div class="tag blue wide">Steak Dinner</div>
    <ul class="list"><li>Pre event Radio advertising</li><li>Company logo on posters</li><li>Social media Ads and mentions</li><li>Company logo on Big screen</li><li>Company logo on Web</li><li>Commercial on the big screen</li><li>2 large Banners (sponsor provided) in arena</li><li>6 weekend passes</li><li>6 Dance tickets (must be age of majority) including steak dinner</li></ul>
  </div>

  <div class="abs foot-blue" style="top:480px"></div>
  <div class="abs foot-green" style="top:480px"></div>
  <div class="abs brand brand-sm" style="left:274px;top:467px">
    <div class="dot"></div><div><div class="name">FENWICK</div><div class="sub">FIRST NATION</div></div>
  </div>
</section>

<!-- Page 4: invoice -->
<section class="page p4">
  <div class="abs inv-head"></div>
  <div class="abs inv-badge">
    <div class="brand brand-sm" style="gap:4px">
      <div class="dot" style="width:12px;height:12px"></div>
      <div><div class="name" style="font-size:8px">FENWICK</div><div class="sub" style="font-size:3.6px">FIRST NATION</div></div>
    </div>
    <h2>SPONSORSHIP<br>INVOICE</h2>
  </div>
  <div class="abs fields">
    <div class="field">Company Name :</div>
    <div class="field">Attention :</div>
    <div class="field">Address :</div>
    <div class="field" style="height:23px;padding-top:8px">Phone Number :</div>
    <div class="field" style="border:none">Date :</div>
  </div>

  <div class="abs tbl" style="top:146px;height:104px">
    <div class="hd"><span style="left:9px">RODEO PACKAGES</span><span style="left:164px">QUANTITY</span><span style="left:255px">COST</span><span style="left:308px">TOTAL</span></div>
    <div class="vl" style="left:125px"></div><div class="vl" style="left:238px"></div><div class="vl" style="left:296px"></div>
    <div style="height:4px"></div>
    <div class="row"><span style="left:4px">Starter Package</span><span style="left:238px">$ 750</span></div>
    <div class="row"><span style="left:4px">Bronze Package</span><span style="left:238px">$ 1,500</span></div>
    <div class="row"><span style="left:4px">Silver Package</span><span style="left:238px">$ 3,000</span></div>
    <div class="row"><span style="left:4px">Gold Package</span><span style="left:238px">$ 5,000</span></div>
    <div class="row" style="border:none"><span style="left:4px">Platinum Package</span><span style="left:238px">$ 7,500</span></div>
  </div>

  <div class="abs tbl" style="top:273px;height:89px">
    <div class="hd"><span style="left:9px">EVENT PACKAGES</span><span style="left:164px">QUANTITY</span><span style="left:255px">COST</span><span style="left:308px">TOTAL</span></div>
    <div class="vl" style="left:125px"></div><div class="vl" style="left:238px"></div><div class="vl" style="left:296px"></div>
    <div style="height:4px"></div>
    <div class="row"><span style="left:4px">Fun Package</span><span style="left:238px">$ 1,000</span></div>
    <div class="row"><span style="left:4px">Dance Saloon Package</span><span style="left:238px">$ 6,000</span></div>
    <div class="row"><span style="left:4px">Steak Dinner Package</span><span style="left:238px">$ 4,000</span></div>
    <div class="row" style="border:none"><span style="left:4px">Pancake Breakfast Package</span><span style="left:238px">$ 2,000</span></div>
  </div>

  <div class="abs pay">
    <div class="abs" style="left:10px;top:9px">Paid by Cheque #</div>
    <div class="abs" style="left:10px;top:26px">Fenwick Creek First Nation</div>
    <div class="abs" style="left:248px;top:5px;text-align:center;line-height:1.15">Total Nation<br>Invoice</div>
    <div class="abs" style="left:8px;right:8px;top:21px;border-top:1px dashed #6f8bab"></div>
    <div class="abs" style="left:125px;top:4px;bottom:4px;border-left:1px dashed #6f8bab"></div>
    <div class="abs" style="left:296px;top:4px;bottom:4px;border-left:1px dashed #6f8bab"></div>
  </div>

  <div class="abs site">www.<b>fenwickcreekfn</b>.com</div>
</section>

</body>
</html>
```